Commercial and Residential landscape Flyer design

we would like a flyer to advertise our new landscaping division for our company. Phone Number 5184620371
email pinecrestgroundworkservices@mailorbit.net
address 7 Marlow Court Schenectady New York 12419
The design is up to you. ill attach some sample flyers in the file section
Target Market(s)
Residential and commercial properties
Industry/Entity Type
Landscape
Font styles to use
Sans Serif
Colors
Designer to choose colors to be used in the design.
Requirements
Must have
- Services offered
- Spring Cleanups
- Mulch installation
- Mowing
- Tree and shrub Maintenance
- Fall Cleanups
- Fully Insured
- Free Estimates
Nice to have
- See word file Please double check all grammar and spelling
- Feel free to use anything in the word file. Its totally up to you. It all doesn't need to be on it . would like to stick with the color scheme of the logo
Should not have
- there are no should not haves. We just want to get the word out that we have a landscape division

```html
<!DOCTYPE html>
<html lang="en">
<head>
<meta charset="utf-8">
<title>Pinecrest Groundwork Services – Landscaping Flyer</title>
<link rel="stylesheet" href="https://fonts.googleapis.com/css2?family=Oswald:wght@600&family=Open+Sans:wght@400;600;700;800&family=Patrick+Hand&display=swap">
<style>
  :root {
    --grass-light: #5fc42a;
    --grass-mid: #45a51c;
    --grass-dark: #2f7d12;
    --olive-panel: rgba(92, 110, 20, 0.55);
    --ink: #0b0b0b;
    --brand-green: #4cc72c;
    --heading-dark: #1d2a10;
    --white: #ffffff;
  }
  * { margin: 0; padding: 0; box-sizing: border-box; }
  html, body { width: 848px; height: 1200px; overflow: hidden; background: #fff; }
  .flyer {
    position: relative; width: 848px; height: 1200px; overflow: hidden;
    font-family: "Open Sans", sans-serif;
  }
  .grass-backdrop {
    position: absolute; inset: 0 0 376px 0;
    background: radial-gradient(ellipse at 20% 30%, var(--grass-light), var(--grass-mid) 55%, var(--grass-dark));
  }
  .frame-lines { position: absolute; left: 0; top: 0; width: 848px; height: 824px; }
  .brand-box {
    position: absolute; left: 34px; top: 0; width: 288px; height: 246px;
    background: var(--ink); display: flex; flex-direction: column;
    align-items: center; justify-content: center; gap: 14px;
  }
  .brand-mark { width: 22px; height: 22px; border-radius: 50%; background: var(--brand-green); }
  .brand-name {
    color: var(--brand-green); font-weight: 800; font-size: 30px; line-height: 1.1;
    text-align: center; text-transform: uppercase;
  }
  .tagline-box {
    position: absolute; left: 34px; top: 254px; width: 288px; height: 139px;
    background: var(--ink); padding: 10px 10px 0 10px;
    color: var(--white); font-weight: 700; font-size: 29px; line-height: 42px;
  }
  .about { position: absolute; left: 15px; top: 432px; width: 392px; color: var(--white); font-family: "Patrick Hand", cursive; }
  .about h2 { font-weight: 400; font-size: 30px; color: var(--ink); margin-bottom: 14px; }
  .about p { font-size: 20px; line-height: 25.3px; }
  .services { position: absolute; left: 400px; top: 12px; width: 448px; }
  .services h1 { font-family: "Oswald", sans-serif; font-weight: 600; font-size: 27px; color: var(--white); line-height: 34px; }
  .services h3 { font-weight: 600; font-size: 21px; color: var(--heading-dark); }
  .service-list { list-style: none; font-family: "Patrick Hand", cursive; color: var(--white); font-size: 23.5px; }
  .yard h3 { margin-top: 4px; }
  .yard .service-list { margin: 13px 0 0 46px; line-height: 29px; }
  .trees { margin-top: 22px; }
  .trees .service-list { margin: 18px 0 0 46px; line-height: 31px; }
  .indent { padding-left: 200px; display: block; }
  .special { margin-top: 20px; }
  .special h3 { margin-left: 29px; }
  .special .service-list { margin: 22px 0 0 52px; line-height: 31px; }
  .gallery { position: absolute; left: 0; top: 824px; width: 848px; height: 248px; background: var(--ink); }
  .photo { position: absolute; }
  .photo-garden { left: 21px; top: 40px; width: 240px; height: 179px; background: linear-gradient(180deg, #7a6a5a 0%, #c25a6a 35%, #4fb32a 60%, #5cc43a 100%); }
  .photo-home { left: 289px; top: 24px; width: 269px; height: 205px; background: linear-gradient(180deg, #a9c9dc 0%, #2f5a2a 35%, #caa45a 50%, #55b02a 70%, #3d8f22 100%); }
  .photo-pool { left: 587px; top: 40px; width: 237px; height: 176px; background: linear-gradient(180deg, #6b8f4a 0%, #4aa8d8 40%, #9c958a 60%, #4fa82a 100%); }
  .grass-strip { position: absolute; left: 0; top: 1072px; width: 848px; height: 11px; background: var(--grass-mid); }
  .contact { position: absolute; left: 0; top: 1083px; width: 848px; height: 117px; background: var(--ink); color: var(--white); }
  .contact h2 { position: absolute; left: 0; width: 848px; top: 8px; text-align: center; color: var(--brand-green); font-weight: 700; font-size: 28px; }
  .phone { position: absolute; left: 22px; top: 44px; font-weight: 700; font-size: 32px; }
  .email { position: absolute; left: 286px; top: 50px; font-size: 24.5px; font-weight: 600; }
  .contact-icon { position: absolute; top: 90px; }
</style>
</head>
<body>
<div class="flyer">
  <div class="grass-backdrop" role="img" aria-label="Close-up of fresh green lawn grass"></div>

  <svg class="frame-lines" viewBox="0 0 848 824" aria-hidden="true">
    <polygon points="392,0 848,0 848,824 418,824" fill="var(--olive-panel)"/>
    <line x1="392" y1="0" x2="418" y2="824" stroke="#0b0b0b" stroke-width="4"/>
    <line x1="0" y1="406" x2="398" y2="402" stroke="#0b0b0b" stroke-width="4"/>
    <line x1="0" y1="815" x2="418" y2="818" stroke="#0b0b0b" stroke-width="4"/>
  </svg>

  <div class="brand-box">
    <span class="brand-mark"></span>
    <span class="brand-name">Pinecrest<br>Groundwork<br>Services</span>
  </div>

  <div class="tagline-box">Commercial<br>and Residential<br>Landscaping</div>

  <section class="about">
    <h2>About us</h2>
    <p>We are a family-owned, family operated business, so we know from experience how important your yard's appearance is to you. We give your yard the same care that we give our own. At the same time, we know that you have your own unique vision for your landscaping, and our design of your yard reflects that. Work with us to create the yard of your dreams.</p>
  </section>

  <section class="services">
    <h1>Our Services</h1>
    <div class="yard">
      <h3>Yard Clean UP services</h3>
      <ul class="service-list">
        <li>-Periodic cleanups</li>
        <li>-Spring cleanups</li>
        <li>-Fall cleanups</li>
        <li>-Special occasion cleanups</li>
        <li>-“I just don't have time” cleanups</li>
      </ul>
    </div>
    <div class="trees">
      <h3>Tree Trimming, Removal &amp; More</h3>
      <ul class="service-list">
        <li>-Tree and shrub removal</li>
        <li>-Single tree removal</li>
        <li>-Tree trimming (hazardous limb <span class="indent">removal and</span><span class="indent">view cutting)</span></li>
        <li>-Installation of new trees, shrubs, perennials, and annuals</li>
      </ul>
    </div>
    <div class="special">
      <h3>Special Services</h3>
      <ul class="service-list">
        <li>-&nbsp; Mulch installation</li>
        <li>-&nbsp; Fully Insured</li>
        <li>-&nbsp; Free Estimates</li>
      </ul>
    </div>
  </section>

  <div class="gallery">
    <div class="photo photo-garden" role="img" aria-label="Curving lawn path between colourful flower beds"></div>
    <div class="photo photo-home" role="img" aria-label="Lit house at dusk with manicured lawn and planting bed"></div>
    <div class="photo photo-pool" role="img" aria-label="Stone-edged garden bed beside a backyard pool"></div>
  </div>

  <div class="grass-strip"></div>

  <footer class="contact">
    <h2>Contact us for your free estimate</h2>
    <div class="phone">518-462-0371</div>
    <div class="email">pinecrestgroundworkservices@mailorbit.net</div>
    <svg class="contact-icon" style="left:124px" width="70" height="30" viewBox="0 0 70 30" aria-hidden="true">
      <rect x="3" y="3" width="64" height="40" rx="4" fill="none" stroke="var(--brand-green)" stroke-width="4"/>
      <rect x="14" y="10" width="24" height="10" fill="var(--brand-green)"/>
    </svg>
    <svg class="contact-icon" style="left:550px" width="64" height="30" viewBox="0 0 64 30" aria-hidden="true">
      <polygon points="2,16 32,2 62,16 62,40 2,40" fill="var(--brand-green)"/>
      <polyline points="2,16 32,32 62,16" fill="none" stroke="#0b0b0b" stroke-width="3"/>
    </svg>
  </footer>
</div>
</body>
</html>
```